bramwick.link bramwick.space bramwick.press website

The website is named BRAMWICK and it will have 3 domain names. bramwick.link, press, space.
I'd like it to be viewed on Pads, pcs and phones.

page menu:

bramwick.link(start page): presentation of company. (creative, design, app, new product innovation.)
Here we'll need sosial media icons: vextro, pollumax, gorvida, tenkoral. (light but some 'fruity' colors)

bramwick.press: blog. It will be a 75% picture blog > rest will be text. I need to be able to resize pictures and shape columns to picture size. (light but some 'fruity' colors)

bramwick.space : the fun part of this web design, however, on entering the page I'd like a non-disclosure agreement where viewer simply click "yes, I agree" after filling out contact info. (check attached document)
We will have space here for uploading PDF files viewers can download. There is also a blog space here to tell in brief about the PDF file. (maybe a space/sci-fi theme her e.g spacechimp, Vessa the space dog?)

I will attach the logo here I want you to use > and develop for the .space .press webpage. The logo i uploaded is for the .link page.

Target Market(s)

venture capitalists

Number of Pages Required

3 page

Requirements
Must have
• a few 'fruity colors' but mostly white and grey

```html
<!DOCTYPE html>
<html lang="en">
<head>
<meta charset="utf-8">
<title>BRAMWICK — Creative Design and App Creation</title>
<link rel="stylesheet" href="https://fonts.googleapis.com/css2?family=Silkscreen:wght@400;700&family=Open+Sans:wght@400;600;700&display=swap">
<style>
  :root{
    --purple:#5d4889;
    --purple-deep:#3b2f5c;
    --red:#e8474c;
    --green:#7cb342;
    --green-light:#8fc94f;
    --grey-btn:#8e8e8e;
    --ink:#333333;
    --muted:#8a8a8a;
    --paper:#f4f4f4;
    --white:#ffffff;
    --slate:#4b535e;
    --blue:#2a9fd8;
    --orange:#f7a11a;
    --tomato:#f26b3a;
    --amber:#f58c1e;
    --crimson:#e53935;
    --yellow:#f5c518;
    --pixel:'Silkscreen', monospace;
    --sans:'Open Sans', sans-serif;
  }
  *{box-sizing:border-box;margin:0;padding:0}
  html,body{width:1200px;height:3333px;overflow:hidden}
  body{font-family:var(--sans);color:var(--ink);background:var(--white);position:relative}
  section,nav,footer{position:absolute;left:0;width:1200px;overflow:hidden}
  .abs{position:absolute}

  /* hero */
  .hero{top:0;height:573px;background:linear-gradient(90deg,var(--purple) 0%,#5a4785 62%,#47395f 80%,#2a2632 100%)}
  .hero .bubble{position:absolute;border-radius:50%;background:rgba(255,255,255,.06)}
  .brand{left:255px;top:108px;display:flex;align-items:center;gap:12px}
  .brand .mark{width:22px;height:22px;background:var(--orange)}
  .brand .name{font-family:var(--pixel);font-weight:700;font-size:30px;line-height:1;color:var(--white);white-space:nowrap}
  .hero h1{left:48px;top:288px;width:620px;text-align:center;font-family:var(--pixel);font-weight:700;font-size:26px;line-height:30px;color:var(--white);white-space:nowrap}
  .hero .tagline{left:48px;top:322px;width:620px;text-align:center;font-family:var(--pixel);font-size:15px;line-height:18px;color:#cdc3e6;white-space:nowrap}
  .available{font-size:11px;font-weight:700;color:var(--white);letter-spacing:.5px;text-transform:uppercase}
  .hero .available{left:171px;top:378px;width:353px;text-align:center}
  .store-btn{display:flex;align-items:center;gap:10px;padding-left:14px;color:var(--white);height:46px;border-radius:3px}
  .store-btn .dot{width:20px;height:20px;border-radius:50%;background:var(--white);flex:none}
  .store-btn b{display:block;font-size:11px;letter-spacing:.3px}
  .store-btn small{display:block;font-size:8px;letter-spacing:.3px;opacity:.9}
  .store-btn.grey{background:var(--grey-btn)}
  .store-btn.green{background:var(--green)}
  .device-showcase{left:707px;top:55px;width:493px;height:467px;border-radius:14px 0 0 14px;background:linear-gradient(135deg,#2c2a36,#4d4a5c 60%,#1f1d25)}

  /* nav */
  .main-nav{top:573px;height:56px;background:var(--red);display:flex;justify-content:center;align-items:center;gap:34px;font-size:12px;color:var(--white);text-transform:uppercase;letter-spacing:.3px}
  .main-nav .sep{opacity:.9}

  /* intro */
  .intro{top:629px;height:515px;background:var(--paper)}
  .intro .phones{left:82px;top:78px;width:518px;height:437px;border-radius:26px 26px 0 0;background:linear-gradient(120deg,#cfd6de,#7d9bb3 45%,#2b2b30 60%,#e8a58a 100%)}
  .intro h2{left:638px;top:100px;width:540px;font-family:var(--pixel);font-weight:700;font-size:23px;line-height:32px;color:var(--red);white-space:nowrap}
  .intro .lead{left:644px;top:196px;width:505px;font-size:16.5px;line-height:25px;color:var(--ink)}
  .intro .body{left:644px;top:300px;width:505px;font-size:13px;line-height:21px;color:var(--muted)}
  .btn-more{left:649px;top:387px;width:171px;height:46px;border-radius:23px;background:var(--green);color:var(--white);font-size:12px;font-weight:700;text-transform:uppercase;display:flex;align-items:center;padding-left:52px}
  .btn-more .arrow{position:absolute;right:6px;top:6px;width:34px;height:34px;border-radius:50%;background:var(--white);display:flex;align-items:center;justify-content:center}

  /* features */
  .features{top:1144px;height:812px;background:radial-gradient(ellipse at 45% 50%,#6b6f63 0%,#4e5660 45%,#3f4650 100%)}
  .section-title{position:absolute;left:0;width:1200px;text-align:center;font-family:var(--pixel);font-weight:700;font-size:27px;line-height:34px;white-space:nowrap}
  .section-sub{position:absolute;left:0;width:1200px;text-align:center;font-size:14px}
  .features .section-title{top:70px;color:var(--white)}
  .features .section-sub{top:122px;color:#d5d8de}
  .app-phone{left:489px;top:216px;width:227px;height:533px;border-radius:34px;background:var(--white);padding:74px 12px 80px}
  .app-phone .screen{width:100%;height:100%;background:linear-gradient(180deg,#9cc35a,#6f9a3c 60%,#b9c98a)}
  .app-phone .speaker{position:absolute;left:88px;top:34px;width:50px;height:5px;border-radius:3px;background:#cfcfcf}
  .app-phone .home{position:absolute;left:95px;top:466px;width:38px;height:38px;border-radius:50%;border:2px solid #cfcfcf}
  .feature{position:absolute;width:400px}
  .feature h3{font-size:14px;font-weight:700;color:var(--white);margin-bottom:12px}
  .feature p{font-size:11.5px;line-height:18px;color:#d9dce2}
  .feature.left{text-align:right}
  .tile{position:absolute;width:96px;height:96px;border-radius:16px;display:flex;align-items:center;justify-content:center;box-shadow:6px 8px 0 rgba(0,0,0,.25)}

  /* screenshots */
  .screens{top:1956px;height:662px;background:var(--white)}
  .screens .section-title{top:68px;color:var(--red);font-size:29px}
  .screens .section-sub{top:133px;color:var(--muted)}
  .shot{top:195px;width:200px;height:353px;border:1px solid #dcdcdc;box-shadow:0 2px 6px rgba(0,0,0,.12)}
  .shot.a{left:82px;background:linear-gradient(180deg,#7cb342 0 9%,#f5f5f5 9% 14%,#b86a4a 14% 40%,#3f7fb8 40% 66%,#2f3a45 66%)}
  .shot.b{left:360px;background:linear-gradient(180deg,#7cb342 0 9%,#ffffff 9% 62%,#c0463e 62% 100%)}
  .shot.c{left:638px;background:linear-gradient(180deg,#7cb342 0 9%,#ffffff 9% 18%,#6fa2b8 18% 64%,#ffffff 64%)}
  .shot.d{left:916px;background:linear-gradient(180deg,#222 0 9%,#2d2d2d 9% 44%,#7cb342 44% 50%,#2d2d2d 50%)}
  .pager{position:absolute;left:0;top:601px;width:1200px;display:flex;justify-content:center;gap:14px}
  .pager span{width:10px;height:10px;border-radius:50%;border:1.5px solid #9a9a9a}
  .pager span.on{background:#9a9a9a}

  /* newsletter */
  .newsletter{top:2618px;height:393px;background:linear-gradient(180deg,var(--green-light),#7cbf3d)}
  .newsletter .bubble{position:absolute;border-radius:50%;background:rgba(0,0,0,.05)}
  .newsletter .section-title{top:110px;color:var(--white);font-size:29px}
  .newsletter .section-title em{font-style:normal;color:var(--red)}
  .newsletter .note{position:absolute;left:360px;top:168px;width:480px;text-align:center;font-size:12.5px;line-height:20px;color:#d6ecbf}
  .signup{position:absolute;left:344px;top:233px;display:flex;gap:5px}
  .signup .field{width:367px;height:38px;border-radius:19px;background:var(--white);display:flex;align-items:center;justify-content:space-between;padding:0 18px 0 22px;font-size:11px;color:#9a9a9a}
  .signup .subscribe{width:131px;height:38px;border-radius:19px;background:var(--red);color:var(--white);font-size:11px;font-weight:700;display:flex;align-items:center;justify-content:center;text-transform:uppercase}

  /* footer */
  .site-footer{top:3011px;height:322px;background:var(--white)}
  .mail-tab{left:555px;top:-45px;width:90px;height:90px;border-radius:50%;background:#d9d9d9;display:flex;align-items:flex-end;justify-content:center;padding-bottom:10px}
  .site-footer .available{left:0;top:78px;width:1200px;text-align:center;color:#666;font-size:10px}
  .socials{position:absolute;left:0;top:211px;width:1200px;display:flex;justify-content:center;gap:26px}
  .socials span{width:52px;height:52px;border-radius:50%;display:flex;align-items:center;justify-content:center;color:var(--white);font-weight:700;font-size:17px}
</style>
</head>
<body>

<section class="hero">
  <div class="bubble" style="left:300px;top:-120px;width:300px;height:300px"></div>
  <div class="bubble" style="left:60px;top:330px;width:180px;height:180px"></div>
  <div class="bubble" style="left:380px;top:470px;width:120px;height:120px"></div>
  <div class="bubble" style="left:560px;top:430px;width:90px;height:90px"></div>

  <div class="abs brand"><span class="mark"></span><span class="name">BRAMWICK</span></div>
  <h1 class="abs">WE PROVIDE CREATIVE DESIGN</h1>
  <p class="abs tagline">AND APP CREATION, NEW PRODUCT INNOVATION ETC</p>
  <p class="abs available">Available on:</p>
  <a class="abs store-btn grey" style="left:171px;top:407px;width:167px"><span class="dot"></span><span><b>DOWNLOAD APP</b><small>FROM APPVAULT</small></span></a>
  <a class="abs store-btn green" style="left:358px;top:407px;width:166px"><span class="dot"></span><span><b>DOWNLOAD APP</b><small>FROM PLAYGROVE</small></span></a>

  <div class="abs device-showcase" role="img" aria-label="Laptop and tablet showing the app's feature list screens"></div>
</section>

<nav class="main-nav">
  <span>Home</span><span class="sep">/</span>
  <span>About us</span><span class="sep">/</span>
  <span>Products</span><span class="sep">/</span>
  <span>App features</span><span class="sep">/</span>
  <span>Blog</span><span class="sep">/</span>
  <span>Contact us</span>
</nav>

<section class="intro">
  <div class="abs phones" role="img" aria-label="Three smartphones showing travel photographs"></div>
  <h2 class="abs">APP CREATION AND NEW PRODUCT<br>INNOVATION ETC</h2>
  <p class="abs lead">Lorem ipsum dolor sit amet, consectetur adipiscing elit. Pellentesque vitae arcu sit amet urna sagittis consectetur in a ante. Suspendisse potenti.</p>
  <p class="abs body">Cum sociis natoque penatibus et magnis dis parturient montes, nascetur ridiculus mus. Duis semper erat quis nisi blandit, ut suscipit sem porta.</p>
  <a class="abs btn-more">Read more
    <span class="arrow"><svg width="16" height="16" viewBox="0 0 16 16"><path d="M3 8h9M8 4l4 4-4 4" stroke="#7cb342" stroke-width="2.2" fill="none" stroke-linecap="round"/></svg></span>
  </a>
</section>

<section class="features">
  <h2 class="section-title">BRILLIANT FEATURES</h2>
  <p class="section-sub">Revolutionary Mobile Marketing Software Platform Features</p>

  <div class="abs app-phone" role="img" aria-label="Phone displaying the app start screen">
    <span class="speaker"></span>
    <div class="screen"></div>
    <span class="home"></span>
  </div>

  <div class="feature left" style="left:-84px;top:240px">
    <h3>Mobile Text Message Marketing</h3>
    <p>Mobile Text Message Marketing makes up<br>the foundation of Marketing at Reachline</p>
  </div>
  <div class="feature left" style="left:-84px;top:418px">
    <h3>Bulk SMS Service</h3>
    <p>Businesses and organizations utilize<br>Marketing at Reachline to reach people</p>
  </div>
  <div class="feature left" style="left:-84px;top:584px">
    <h3>Mobile Keyword Technology</h3>
    <p>Setup as many Mobile Keywords as you'd<br>like in minutes. When people text the</p>
  </div>

  <div class="tile" style="left:357px;top:230px;background:var(--blue)">
    <svg width="48" height="44" viewBox="0 0 48 44"><path d="M6 4h36a4 4 0 0 1 4 4v20a4 4 0 0 1-4 4H20l-10 9v-9H6a4 4 0 0 1-4-4V8a4 4 0 0 1 4-4z" fill="#fff"/></svg>
  </div>
  <div class="tile" style="left:357px;top:408px;background:var(--orange)">
    <svg width="40" height="44" viewBox="0 0 40 44"><path d="M20 4c-8 0-13 6-13 14v10l-4 6h34l-4-6V18c0-8-5-14-13-14z" fill="#fff"/><circle cx="20" cy="39" r="4" fill="#fff"/></svg>
  </div>
  <div class="tile" style="left:357px;top:574px;background:var(--tomato)">
    <svg width="36" height="44" viewBox="0 0 36 44"><path d="M4 2h20l10 10v30H4z" fill="#fff"/><path d="M10 20h16M10 27h16M10 34h12" stroke="var(--tomato)" stroke-width="3"/></svg>
  </div>

  <div class="tile" style="left:751px;top:230px;background:var(--amber)">
    <svg width="46" height="46" viewBox="0 0 46 46"><circle cx="23" cy="25" r="17" fill="#fff"/><path d="M23 15v11l7 5" stroke="var(--amber)" stroke-width="3.5" fill="none" stroke-linecap="round"/></svg>
  </div>
  <div class="tile" style="left:751px;top:408px;background:var(--crimson)">
    <svg width="46" height="46" viewBox="0 0 46 46"><circle cx="23" cy="23" r="18" fill="#fff"/><circle cx="23" cy="23" r="8" fill="var(--crimson)"/></svg>
  </div>
  <div class="tile" style="left:751px;top:574px;background:var(--yellow)">
    <svg width="46" height="46" viewBox="0 0 46 46"><g fill="#fff"><circle cx="23" cy="23" r="14"/><rect x="19" y="3" width="8" height="40" rx="2"/><rect x="3" y="19" width="40" height="8" rx="2"/><rect x="19" y="3" width="8" height="40" rx="2" transform="rotate(45 23 23)"/><rect x="19" y="3" width="8" height="40" rx="2" transform="rotate(-45 23 23)"/></g><circle cx="23" cy="23" r="6" fill="var(--yellow)"/></svg>
  </div>

  <div class="feature" style="left:871px;top:240px;width:300px">
    <h3>Lorem ipsum dolor sit amet</h3>
    <p>Our mobile text messaging reminder<br>feature allows you to easily queue and send</p>
  </div>
  <div class="feature" style="left:871px;top:418px;width:300px">
    <h3>Mobile Coupons</h3>
    <p>You can offer free gifts, discounts,<br>incentives, and reminders to your</p>
  </div>
  <div class="feature" style="left:871px;top:584px;width:300px">
    <h3>Pellentesque vitae arcu sit amet</h3>
    <p>You can offer free gifts, discounts,<br>incentives, and reminders to your</p>
  </div>
</section>

<section class="screens">
  <h2 class="section-title">SCREENSHOTS</h2>
  <p class="section-sub">Showcase your app screenshots into a nice carousel below. You can add as many screenshots as you want.</p>
  <div class="abs shot a" role="img" aria-label="App screenshot: grid of shots feed"></div>
  <div class="abs shot b" role="img" aria-label="App screenshot: user profile"></div>
  <div class="abs shot c" role="img" aria-label="App screenshot: single shot detail"></div>
  <div class="abs shot d" role="img" aria-label="App screenshot: side menu"></div>
  <div class="pager"><span></span><span></span><span class="on"></span><span></span><span></span></div>
</section>

<section class="newsletter">
  <div class="bubble" style="left:130px;top:30px;width:190px;height:190px"></div>
  <div class="bubble" style="left:840px;top:20px;width:150px;height:150px"></div>
  <div class="bubble" style="left:230px;top:290px;width:110px;height:110px"></div>
  <div class="bubble" style="left:700px;top:280px;width:120px;height:120px"></div>
  <h2 class="section-title">KNOW THE LATEST NEWS OF <em>BRAMWICK</em></h2>
  <p class="note">Donec vulputate, urna ut volutpat pretium, quam diam varius nunc, sed fermentum metus urna sed nulla nulla vel magna viverra</p>
  <div class="signup">
    <span class="field">Enter Your Email Address
      <svg width="16" height="12" viewBox="0 0 16 12"><rect x="1" y="1" width="14" height="10" rx="1" fill="none" stroke="#7cb342" stroke-width="1.5"/><path d="M1 1l7 6 7-6" fill="none" stroke="#7cb342" stroke-width="1.5"/></svg>
    </span>
    <span class="subscribe">Subscribe</span>
  </div>
</section>

<footer class="site-footer">
  <div class="abs mail-tab">
    <svg width="26" height="18" viewBox="0 0 26 18"><rect x="1" y="1" width="24" height="16" rx="2" fill="#fff"/><path d="M1 2l12 9 12-9" fill="none" stroke="#d9d9d9" stroke-width="2"/></svg>
  </div>
  <p class="abs available">Available on</p>
  <a class="abs store-btn grey" style="left:398px;top:116px;width:193px;height:51px"><span class="dot"></span><span><b>DOWNLOAD APP</b><small>FROM APPVAULT</small></span></a>
  <a class="abs store-btn green" style="left:611px;top:116px;width:191px;height:51px"><span class="dot"></span><span><b>DOWNLOAD APP</b><small>FROM PLAYGROVE</small></span></a>
  <div class="socials">
    <span style="background:var(--crimson)" aria-label="gorvida">G</span>
    <span style="background:var(--orange)" aria-label="vextro">V</span>
    <span style="background:#1e88c9" aria-label="pollumax">P</span>
    <span style="background:var(--yellow)" aria-label="tenkoral">T</span>
  </div>
</footer>

</body>
</html>
```